RM Dorvanta businesscard project

RM Dorvanta Ltd is a freshly founded small (3 employees), young (average age is 30 years) company, living from the road transportation market without own tools.
We would like to have an impressive, new-line, cool busines card for a freshly founded forwarding company on an overcrowded market which raises attention and makes the potential partners eager to work with us.

Target Market(s)

The main profile of the company is logistic/forwarding on road.

Industry/Entity Type

Freight Forwarding

Contact Information for Business Card

Name: Berki Zsófia
Title: general manager
mobile nr: +36-70/482-5193
fax nr: +36-1/534-9061
e-mail: zsofia.berki@rmdorvanta.example
info@rmdorvanta.example
website address: http://www.rmdorvanta.example
and if possible maybe some funny or helpful info on the back

Requirements
Must have
• contact details above
Nice to have
• some really nice and catching back-side (info, graphics, useful tool info... anything)
Should not have
• trucks, road, ship, airplane on it...

```html
<!DOCTYPE html>
<html lang="hu">
<head>
<meta charset="utf-8">
<title>RM Dorvanta – business card</title>
<link href="https://fonts.googleapis.com/css2?family=Roboto+Condensed:wght@300;400&display=swap" rel="stylesheet">
<style>
  :root {
    --brand-blue: #4d7bb5;
    --ink: #1f1f1f;
    --ink-soft: #4a4a4a;
    --paper: #ffffff;
    --backdrop: #dedede;
    --shadow: rgba(40, 70, 80, 0.55);
  }
  * { box-sizing: border-box; margin: 0; padding: 0; }
  html, body {
    width: 960px; height: 1200px; overflow: hidden;
    background: var(--backdrop);
    font-family: "Roboto Condensed", "Arial Narrow", sans-serif;
  }
  .canvas { position: relative; width: 960px; height: 1200px; }
  .card {
    position: absolute; top: 798px;
    width: 400px; height: 237px;
  }
  .card::after {
    content: ""; position: absolute; left: 8px; right: 8px; bottom: -14px; height: 14px;
    background: radial-gradient(ellipse at 50% 0%, var(--shadow), transparent 70%);
    filter: blur(3px); z-index: -1;
  }
  .card--front { left: 70px; background: var(--paper); }
  .card--back { left: 506px; background: var(--brand-blue); }

  .brand {
    position: absolute; left: 20px; top: 62px; width: 166px;
    display: flex; flex-direction: column; align-items: center; gap: 14px;
  }
  .brand__square { width: 60px; height: 60px; background: var(--brand-blue); }
  .brand__name {
    font-weight: 400; font-size: 30px; line-height: 1; color: var(--ink);
    letter-spacing: -0.5px; white-space: nowrap;
  }

  .contact { position: absolute; left: 216px; top: 32px; width: 176px; color: var(--ink); }
  .contact__name { font-size: 16px; font-weight: 400; line-height: 1.1; }
  .contact__title { font-size: 12px; font-weight: 300; color: var(--ink-soft); margin-top: 2px; }
  .contact__mobile { display: flex; gap: 11px; margin-top: 13px; }
  .contact__mobile .numbers { line-height: 1.3; }
  .contact__mobile .phone { font-size: 15px; }
  .contact__mobile .mail { font-size: 11px; font-weight: 300; white-space: nowrap; }
  .contact__list { list-style: none; margin-top: 13px; }
  .contact__list li { display: flex; align-items: center; gap: 12px; font-size: 13px; height: 21.5px; white-space: nowrap; }
  .icon { flex: none; fill: var(--ink); }

  .back-brand {
    position: absolute; inset: 0;
    display: flex; align-items: center; justify-content: center; gap: 14px;
  }
  .back-brand__square { width: 34px; height: 34px; background: var(--paper); }
  .back-brand__name { font-size: 40px; font-weight: 400; color: var(--paper); letter-spacing: -0.5px; }
</style>
</head>
<body>
<main class="canvas">
  <section class="card card--front" aria-label="Business card front">
    <div class="brand">
      <span class="brand__square"></span>
      <span class="brand__name">RM Dorvanta</span>
    </div>
    <div class="contact">
      <p class="contact__name">Berki Zsófia</p>
      <p class="contact__title">General Manager</p>
      <div class="contact__mobile">
        <svg class="icon" width="13" height="26" viewBox="0 0 13 26" aria-hidden="true">
          <rect x="0.8" y="0.8" width="11.4" height="24.4" rx="2" fill="none" stroke="#1f1f1f" stroke-width="1.6"/>
          <circle cx="6.5" cy="22" r="1.2"/>
          <path d="M4 15 q0-6 5-8" fill="none" stroke="#1f1f1f" stroke-width="1.6"/>
        </svg>
        <div class="numbers">
          <p class="phone">+36-70 / 482-5193</p>
          <p class="mail">zsofia.berki@rmdorvanta.example</p>
        </div>
      </div>
      <ul class="contact__list">
        <li>
          <svg class="icon" width="13" height="13" viewBox="0 0 13 13" aria-hidden="true">
            <rect x="1" y="3" width="11" height="9" rx="1.5" fill="none" stroke="#1f1f1f" stroke-width="1.4"/>
            <rect x="3" y="0.5" width="7" height="3" rx="1"/>
            <path d="M3.5 6h6M3.5 8h6M3.5 10h6" stroke="#1f1f1f" stroke-width="1"/>
          </svg>
          <span>+36-1 / 534-9061</span>
        </li>
        <li>
          <svg class="icon" width="13" height="10" viewBox="0 0 13 10" aria-hidden="true">
            <rect x="0.7" y="0.7" width="11.6" height="8.6" fill="none" stroke="#1f1f1f" stroke-width="1.4"/>
            <path d="M0.7 0.7 6.5 5.5 12.3 0.7M0.7 9.3 5 4.5M12.3 9.3 8 4.5" fill="none" stroke="#1f1f1f" stroke-width="1.2"/>
          </svg>
          <span>info@rmdorvanta.example</span>
        </li>
        <li>
          <svg class="icon" width="13" height="13" viewBox="0 0 13 13" aria-hidden="true">
            <circle cx="6.5" cy="6.5" r="5.8" fill="none" stroke="#1f1f1f" stroke-width="1.3"/>
            <path d="M3 3.5c2 0 2 2 4 2s1 3 3 3M5 9.5c0-2 2-2 2-3"/>
          </svg>
          <span>www.rmdorvanta.example</span>
        </li>
      </ul>
    </div>
  </section>

  <section class="card card--back" aria-label="Business card back">
    <div class="back-brand">
      <span class="back-brand__square"></span>
      <span class="back-brand__name">RM Dorvanta</span>
    </div>
  </section>
</main>
</body>
</html>
```